Design some Business Cards for Tovi Plumber Hub

I would like a business card and sticker designed for our plumbing company. We already have graphics that we would like included in the card.

Please view the attachments.

Business Card- The ai file attached has the basic information I would like on the cards. I just want to make it look a bit more professional.

Sticker - The attachement "Tovi Water Heater [login to view URL]" is the correct size for the sticker. I would like to change the name to Tovi Plumber Hub and use the "[login to view URL]" attachment. It should also say "$100 of your next water heater."

```html
<!DOCTYPE html>
<html lang="en">
<head>
<meta charset="utf-8">
<title>Tovi Plumber Hub – Business Card</title>
<link rel="stylesheet" href="https://fonts.googleapis.com/css2?family=Lato:wght@300;400&display=swap">
<style>
  :root {
    --bg-light: #f4f4f5;
    --bg-mid: #dcdde0;
    --accent-red: #d3121c;
    --band-red: #c10f18;
    --deep-red: #8a0a10;
    --ring-blue: #2f8fd6;
    --mascot-tone: #9ea3a8;
    --name-grey: #3a3b3e;
    --subtitle-grey: #5e6064;
    --white: #ffffff;
  }
  * { margin: 0; padding: 0; box-sizing: border-box; }
  html, body { width: 1200px; height: 685px; overflow: hidden; background: #ffffff; }
  .card {
    position: relative;
    width: 1200px;
    height: 685px;
    overflow: hidden;
    background: radial-gradient(ellipse at 55% 40%, var(--bg-light) 0%, var(--bg-mid) 100%);
    font-family: "Lato", Arial, sans-serif;
  }
  .top-rule {
    position: absolute; left: 0; top: 0; width: 100%; height: 7px;
    background: var(--accent-red);
  }
  .mascot-ring {
    position: absolute; left: 40px; top: 164px; width: 334px; height: 334px;
  }
  .brand-name {
    position: absolute; left: 452px; top: 234px;
    font-size: 68px; font-weight: 400; line-height: 1;
    color: var(--name-grey);
    white-space: nowrap;
  }
  .brand-tagline {
    position: absolute; left: 454px; top: 316px;
    font-size: 34px; font-weight: 400; line-height: 1;
    font-variant: small-caps; letter-spacing: 4px;
    color: var(--subtitle-grey); white-space: nowrap;
  }
  .contact-band {
    position: absolute; left: 0; top: 540px; width: 100%; height: 145px;
    background: linear-gradient(90deg, var(--accent-red) 0%, var(--band-red) 55%, var(--deep-red) 100%);
    color: var(--white);
  }
  .person-name {
    position: absolute; left: 67px; top: 47px;
    font-size: 41px; font-weight: 300; white-space: nowrap;
  }
  .contact-details {
    position: absolute; left: 808px; top: 8px;
    white-space: nowrap;
  }
  .contact-role { font-size: 23px; font-weight: 400; line-height: 34px; }
  .contact-phone { font-size: 43px; font-weight: 300; line-height: 54px; }
  .contact-email { font-size: 21px; font-weight: 400; line-height: 30px; }
</style>
</head>
<body>
<div class="card">
  <div class="top-rule"></div>

  <svg class="mascot-ring" viewBox="0 0 334 334" role="img" aria-label="Cartoon plumber mascot in cap and work shirt holding a red pipe wrench">
    <circle cx="167" cy="167" r="162" fill="var(--mascot-tone)" fill-opacity="0.35" stroke="var(--ring-blue)" stroke-width="6"/>
  </svg>

  <div class="brand-name">Tovi Plumber Hub</div>
  <div class="brand-tagline">Licensed Master Plumber</div>

  <div class="contact-band">
    <div class="person-name">Marlon Vesey</div>
    <div class="contact-details">
      <div class="contact-role">Residential Service Contractor</div>
      <div class="contact-phone">(555) 384-2716</div>
      <div class="contact-email">office@tovihub.net</div>
    </div>
  </div>
</div>
</body>
</html>
```